British Columbia Day banner showcasing 20% off site

Banner graphic promoting our BC Day sale
Size: 1800 x 1000
- flag has been uploaded for inspiration
- examples from other companies and their sale banners have been uploaded for inspiration.
- product images can be found at www.mygreenleafhub.com, please use a variety of different products in this banner

Target Market(s)

19+

Industry/Entity Type

Cannabis

Requirements
Must have
• Phrases:
- “Celebrate BC Day with BC bud and companies”
- “20% off site wide sale*"
- Underneath phrase the date of sale “July 30th - August 3rd”
- In tiny print “*excludes all sale and bundled items”
- MUST BE 1800 X1000
Nice to have
• - images of the products or bud we carry which can be found at www.mygreenleafhub.com
- bold
Should not have
• - company logo

```html
<!DOCTYPE html>
<html lang="en">
<head>
<meta charset="utf-8">
<title>BC Day Sale Banner</title>
<link rel="stylesheet" href="https://fonts.googleapis.com/css2?family=Alfa+Slab+One&family=Quicksand:wght@300;700&display=swap">
<style>
  :root {
    --page: #ffffff;
    --teal-light: #2ba3c4;
    --teal-mid: #1f7f9b;
    --teal-dark: #12536a;
    --bud-green: rgba(70, 130, 70, 0.85);
    --bud-dark: rgba(35, 80, 60, 0.55);
    --tin: #1b3f4a;
    --tin-edge: #0e2a33;
    --pack: rgba(40, 88, 92, 0.75);
    --gummy-green: rgba(95, 160, 75, 0.8);
    --gummy-blue: rgba(60, 140, 165, 0.7);
    --text-light: #f4f8f8;
    --ink: #111111;
  }
  * { margin: 0; padding: 0; box-sizing: border-box; }
  html, body { width: 1200px; height: 720px; overflow: hidden; background: var(--page); }
  .canvas { position: relative; width: 1200px; height: 720px; }
  .banner {
    position: absolute; left: 100px; top: 36px; width: 1000px; height: 556px;
    overflow: hidden;
    background: radial-gradient(ellipse at 50% 55%, var(--teal-light) 0%, var(--teal-mid) 50%, var(--teal-dark) 100%);
  }
  .photo { position: absolute; }
  .bud {
    background: radial-gradient(ellipse closest-side at 50% 50%, var(--bud-green) 0%, var(--bud-dark) 70%, transparent 100%);
  }
  .tin {
    border-radius: 50%;
    background: radial-gradient(circle, var(--tin) 62%, var(--tin-edge) 100%);
  }
  .pack {
    background: radial-gradient(ellipse closest-side, var(--pack) 0%, rgba(40, 88, 92, 0.45) 75%, transparent 100%);
  }
  .gummies-pair {
    background: radial-gradient(ellipse closest-side, var(--gummy-green) 0%, rgba(95, 160, 75, 0.35) 70%, transparent 100%);
  }
  .gummy-cubes {
    border-radius: 16px;
    background: linear-gradient(90deg, var(--gummy-green) 0%, var(--gummy-blue) 55%, rgba(44, 111, 128, 0.5) 100%);
    opacity: .7;
  }
  .headline {
    position: absolute; left: 0; top: 16px; width: 100%;
    font-family: "Alfa Slab One", serif; font-size: 56px; line-height: 68px;
    color: var(--text-light); text-align: center; letter-spacing: 1px;
    font-weight: 400;
  }
  .headline span { display: block; }
  .headline .line-two { padding-left: 28px; }
  .offer {
    position: absolute; left: 206px; top: 268px;
    font-family: "Quicksand", sans-serif; font-weight: 300; font-size: 61px;
    color: var(--text-light); white-space: nowrap;
  }
  .dates {
    position: absolute; right: 38px; top: 360px;
    font-family: "Quicksand", sans-serif; font-weight: 300; font-size: 36px;
    color: var(--text-light); white-space: nowrap;
  }
  .brand {
    position: absolute; left: 413px; top: 500px; width: 174px; text-align: center;
    font-family: "Quicksand", sans-serif; font-weight: 700; font-size: 24px;
    color: var(--ink);
  }
  .fine-print {
    position: absolute; right: 24px; top: 530px;
    font-family: "Quicksand", sans-serif; font-weight: 300; font-size: 18px;
    color: var(--text-light); white-space: nowrap;
  }
</style>
</head>
<body>
<div class="canvas">
  <section class="banner">
    <div class="photo bud" role="img" aria-label="Cannabis bud" style="left:-20px;top:-20px;width:200px;height:150px;"></div>
    <div class="photo bud" role="img" aria-label="Cannabis bud" style="left:312px;top:-20px;width:122px;height:60px;"></div>
    <div class="photo bud" role="img" aria-label="Large cannabis bud" style="left:412px;top:58px;width:196px;height:226px;"></div>
    <div class="photo bud" role="img" aria-label="Cannabis bud" style="left:712px;top:-20px;width:262px;height:236px;"></div>
    <div class="photo bud" role="img" aria-label="Cannabis bud" style="left:152px;top:130px;width:122px;height:150px;"></div>
    <div class="photo bud" role="img" aria-label="Cannabis bud" style="left:852px;top:246px;width:160px;height:120px;"></div>
    <div class="photo bud" role="img" aria-label="Cannabis bud" style="left:262px;top:462px;width:124px;height:110px;"></div>
    <div class="photo tin" role="img" aria-label="Tin of strawberry cannabis edibles" style="left:-12px;top:178px;width:113px;height:140px;"></div>
    <div class="photo pack" role="img" aria-label="Packaged cannabis edible product" style="left:40px;top:380px;width:118px;height:144px;"></div>
    <div class="photo gummies-pair" role="img" aria-label="Two green gummies" style="left:156px;top:398px;width:62px;height:106px;"></div>
    <div class="photo gummy-cubes" role="img" aria-label="Assorted cannabis gummy cubes" style="left:720px;top:422px;width:228px;height:90px;"></div>

    <h1 class="headline">
      <span class="line-one">Celebrate BC Day with BC bud</span>
      <span class="line-two">and companies</span>
    </h1>
    <p class="offer">20% off site wide sale*</p>
    <p class="dates">July 30th - August 3rd</p>
    <p class="brand">GreenLeafHub</p>
    <p class="fine-print">*excludes all sale and bundled items</p>
  </section>
</div>
</body>
</html>
```